Bref créative
tri-fold brochures and business card designs
New Bravoline company selling wall panels
marketing material
New company looking for marketing print material for display in retail locations and tradshows.
Home and Garden
Consumers and B2B retailers
tri-fold brochure and business card designs.
Please review website for ideas www.murelune7k.com.
I have most of images as high resolution. I have similar brochure from partner in Australia but would like to diferentiate a little. Be creative.
This image should be used for business card design, I think looks the best, but you will have to play with the black side color and incorporate the logo with contact info.
here is the brochure cover used from our Australia partner but I would like to include same layout of all images but on the inside of brochure, I will need to upload additional 4 designs.
Also I have my own bullet points.
Plimsora logo and my company logo which should be used on back cover to say Plimsora by my company logo..
Plimsora logo
here is Plimsora logo as jpeg, not sure which is needed.
My front cover bullet points
I would like to see how this image could be incorporated on the front cover of brochure where the Logo is positioned..
Try this image on back cover to see how it looks.
Should have my contact info like on website with my company logo. see website.
Images
I would like to see the look of the image boxes look like my catalogue images with the name and tile inset which I will upload
Plimsora tile design images 1 of 2 zip files
Panel inset tiles zip file 2 of 2
I need the 2 page of front side of brochure to have the ecoproduct info from my website www.murelune7k.com

```html
<!DOCTYPE html>
<html lang="en">
<head>
<meta charset="utf-8">
<title>Plimsora Tri-fold Brochure</title>
<link href="https://fonts.googleapis.com/css2?family=Raleway:wght@300;400;600;700&family=Open+Sans:wght@400;600&display=swap" rel="stylesheet">
<style>
  :root{
    --page:#e4e4e2;
    --charcoal:#22262c;
    --slate:#353b44;
    --slate-light:#4a515b;
    --white:#ffffff;
    --paper:#f4f4f2;
    --orange:#e27a22;
    --orange-deep:#b8521a;
    --bamboo:#8fa63a;
    --bamboo-dark:#3f4a1c;
    --text-light:#d8dbe0;
    --text-dark:#2a2d33;
  }
  *{box-sizing:border-box;margin:0;padding:0}
  html,body{width:1200px;height:871px;overflow:hidden;background:var(--page)}
  body{position:relative;font-family:"Open Sans",Arial,sans-serif}
  .spread{position:absolute;left:40px;width:1120px;height:395px;display:flex;box-shadow:0 4px 14px rgba(0,0,0,.25)}
  .spread--outside{top:28px}
  .spread--inside{top:448px}
  .panel{position:relative;width:373.33px;height:100%;overflow:hidden;background:var(--charcoal);color:var(--text-light)}
  .panel + .panel{border-left:1px solid rgba(255,255,255,.08)}
  .swoosh{position:absolute;left:0;top:0;width:100%;height:100%}
  .photo{position:absolute}
  .photo--bamboo{background:linear-gradient(90deg,var(--bamboo-dark),var(--bamboo) 20%,#c9c24a 35%,var(--bamboo-dark) 50%,var(--bamboo) 68%,#d4c64e 82%,var(--bamboo-dark))}
  .photo--orange-wall{background:radial-gradient(circle at 55% 45%,#f6a14a,var(--orange) 40%,var(--orange-deep) 75%,#5a2a12)}
  .photo--living{background:linear-gradient(135deg,#5b5650,#8c857a 40%,#3a3834 75%,#1f1e1c)}
  .photo--panels{background:linear-gradient(135deg,#e9e9e7,#bdbdbb 50%,#f1f1ef)}
  .photo--chair{background:linear-gradient(160deg,#f2f2f0 0%,#dcdcda 45%,var(--orange) 46%,#c85f1d 70%,#efefed 71%)}
  .section-label{position:absolute;background:var(--slate);color:var(--white);font-family:"Raleway",Arial,sans-serif;font-weight:700;font-size:17px;line-height:1.15;padding:8px 14px}
  .body-copy{position:absolute;font-size:7.4px;line-height:1.5}
  .body-copy p + p{margin-top:6px}
  .brand{position:absolute;display:flex;align-items:center;gap:6px;font-family:"Raleway",Arial,sans-serif;font-weight:400;color:var(--white)}
  .brand__mark{width:10px;height:10px;background:var(--white)}
  .contact{position:absolute;font-size:8px;line-height:1.5;color:var(--text-light)}
  .web{position:absolute;font-family:"Raleway",Arial,sans-serif;font-weight:600;color:var(--white)}
  .tagline-bar{position:absolute;left:0;right:0;bottom:22px;height:30px;background:var(--slate);color:var(--white);font-family:"Raleway",Arial,sans-serif;font-weight:700;font-size:15px;display:flex;align-items:center;padding-left:150px}
  .heading{position:absolute;font-family:"Raleway",Arial,sans-serif;font-weight:400;letter-spacing:2px;font-size:16px;color:var(--white)}
  .tile-row{position:absolute;display:grid;grid-template-columns:repeat(8,26px);gap:5px}
  .tile{width:26px;height:26px;background:linear-gradient(135deg,#f0f0ee,#9c9c9a)}
  .tile-caption{font-size:4px;color:var(--text-light);text-align:center;margin-top:1px}
</style>
</head>
<body>

<!-- Outside: back flap, back cover, front cover -->
<section class="spread spread--outside">

  <article class="panel panel--eco">
    <div class="photo photo--bamboo" style="left:0;top:0;width:100%;height:120px" role="img" aria-label="Photo of green bamboo stalks"></div>
    <svg class="swoosh" viewBox="0 0 373 395" preserveAspectRatio="none" aria-hidden="true">
      <path d="M0 100 C120 150 260 90 373 125 L373 140 C260 110 120 170 0 118 Z" fill="var(--white)"/>
    </svg>
    <div class="section-label" style="left:0;top:150px">Eco friendly<br>Wall covering</div>
    <div class="body-copy" style="left:16px;top:210px;width:340px">
      <p>The raw material used for the production of the Plimsora 3D wall panels is the fibrous residue remaining after sugarcane stalks are crushed to extract their juice. The fibrous waste used as the raw material is 100% recycled.</p>
      <p>Bagasse, as a waste product of sugarcane, is one of the world's most renewable resources. Sugarcane can be harvested up to 2 times a year. The total harvest worldwide is more than 1.2 billion metric tons yearly.</p>
      <p>The raw material of the Plimsora 3D wall panels, bagasse, is also compostable and therefore 100% biodegradable. By re-using waste of sugarcane, panels are produced without burning it.</p>
    </div>
  </article>

  <article class="panel panel--back">
    <svg class="swoosh" viewBox="0 0 373 395" preserveAspectRatio="none" aria-hidden="true">
      <path d="M0 40 C100 20 240 90 373 60 L373 95 C240 125 110 55 0 85 Z" fill="var(--white)"/>
      <path d="M0 300 C120 270 260 330 373 290 L373 395 L0 395 Z" fill="var(--slate)"/>
    </svg>
    <div class="brand" style="left:110px;top:130px;font-size:30px"><span class="brand__mark"></span>Plimsora</div>
    <div class="contact" style="left:130px;top:180px">
      Bravoline Pty Ltd<br>
      PO Box 4821, Harlow Bay<br>
      NSW 2091<br><br>
      1300 555 0148<br>
      hello@murelune7k.com
    </div>
    <div class="web" style="left:0;right:0;bottom:30px;text-align:center;font-size:13px">www.murelune7k.com</div>
  </article>

  <article class="panel panel--cover">
    <div class="brand" style="right:28px;top:22px;font-size:30px"><span class="brand__mark"></span>Plimsora</div>
    <div class="body-copy" style="left:150px;top:72px;width:200px">
      <p>Sculpted three dimensional panels for walls<br>
      Made from renewable sugarcane fibre<br>
      Paintable in any colour you choose<br>
      Light, strong and easy to install<br>
      Fully biodegradable and recycled<br>
      Ideal for homes, shops and offices</p>
    </div>
    <div class="photo photo--orange-wall" style="left:0;top:175px;width:100%;height:220px" role="img" aria-label="Photo of an orange lit textured wall panel interior"></div>
    <svg class="swoosh" viewBox="0 0 373 395" preserveAspectRatio="none" aria-hidden="true">
      <path d="M0 150 C110 120 230 200 373 160 L373 178 C230 220 110 140 0 176 Z" fill="var(--white)"/>
      <path d="M0 176 C110 140 230 220 373 178 L373 190 C230 232 110 152 0 188 Z" fill="var(--charcoal)"/>
    </svg>
    <div class="tagline-bar">Bring Your Walls to Life</div>
  </article>
</section>

<!-- Inside: about us, gallery, story -->
<section class="spread spread--inside">

  <article class="panel panel--about">
    <div class="photo photo--living" style="left:0;top:0;width:100%;height:170px" role="img" aria-label="Photo of a living room with a textured feature wall"></div>
    <svg class="swoosh" viewBox="0 0 373 395" preserveAspectRatio="none" aria-hidden="true">
      <path d="M0 30 C60 90 40 150 0 190 Z" fill="var(--white)"/>
      <path d="M0 160 C120 200 260 140 373 175 L373 395 L0 395 Z" fill="var(--charcoal)"/>
      <path d="M0 150 C120 190 260 130 373 165 L373 175 C260 140 120 200 0 160 Z" fill="var(--white)"/>
    </svg>
    <div class="heading" style="left:22px;top:196px">About Us</div>
    <div class="body-copy" style="left:22px;top:222px;width:150px">
      <p>The Plimsora Bravoline 3d panels are designed that when put together form elegant contemporary patterns. They are the new trend in wall covering. After easy installation they can be painted in any colour to suit the colours of your house or business. The result is an exceptional, environmentally friendly wall decor product which creates a stunning, rich and modern look to any interior setting.</p>
    </div>
    <div class="heading" style="left:22px;top:338px;font-size:11px;letter-spacing:3px">Our designs</div>
    <div class="tile-row" style="left:22px;top:356px;grid-template-columns:repeat(10,26px);gap:4px">
      <div class="tile" role="img" aria-label="Tile design sample"></div>
      <div class="tile" role="img" aria-label="Tile design sample"></div>
      <div class="tile" role="img" aria-label="Tile design sample"></div>
      <div class="tile" role="img" aria-label="Tile design sample"></div>
      <div class="tile" role="img" aria-label="Tile design sample"></div>
      <div class="tile" role="img" aria-label="Tile design sample"></div>
      <div class="tile" role="img" aria-label="Tile design sample"></div>
      <div class="tile" role="img" aria-label="Tile design sample"></div>
      <div class="tile" role="img" aria-label="Tile design sample"></div>
      <div class="tile" role="img" aria-label="Tile design sample"></div>
    </div>
  </article>

  <article class="panel panel--gallery" style="background:var(--paper);color:var(--text-dark)">
    <div class="photo photo--panels" style="left:0;top:0;width:170px;height:205px" role="img" aria-label="Photo of white sculpted 3D wall panels"></div>
    <div class="body-copy" style="left:184px;top:18px;width:175px">
      <p>The Plimsora 3D wall panels are easy to apply with standard adhesive directly onto plaster, brick or board. Each panel joins seamlessly with the next, creating a continuous pattern that can cover a single feature wall or an entire room.</p>
    </div>
    <div class="body-copy" style="left:14px;top:222px;width:165px">
      <p>Plimsora introduced their 3D wall panels in Europe in 2010. Since then the range has grown to dozens of patterns for homes, hotels, shops, offices and restaurants, each one finished by hand.</p>
    </div>
    <div class="photo photo--chair" style="left:190px;top:205px;width:183px;height:190px" role="img" aria-label="Photo of an orange chair against a white patterned wall"></div>
  </article>

  <article class="panel panel--story">
    <div class="photo photo--panels" style="left:0;top:0;width:100%;height:150px" role="img" aria-label="Photo of a wave patterned 3D wall panel"></div>
    <svg class="swoosh" viewBox="0 0 373 395" preserveAspectRatio="none" aria-hidden="true">
      <path d="M0 130 C120 170 260 110 373 145 L373 395 L0 395 Z" fill="var(--charcoal)"/>
      <path d="M0 122 C120 162 260 102 373 137 L373 147 C260 112 120 172 0 132 Z" fill="var(--white)"/>
    </svg>
    <div class="body-copy" style="left:22px;top:190px;width:330px">
      <p>Every panel is pressed from sugarcane pulp and dried naturally, giving a smooth surface ready for paint. The panels are light, sound absorbing and safe to handle, making them ideal for both new builds and renovations.</p>
      <p>Choose from our catalogue of patterns, paint them in your own colours and create a wall that becomes the centre of any room. Ask your local retailer for samples today.</p>
    </div>
  </article>
</section>

</body>
</html>
```